Looking for a clean, modern, and professional business card design that reflects Valtrim Systems

The design should include the company logo, contact details, and align with our brand identity. Please use a sophisticated and minimalist style, incorporating [specific colors, if applicable]. Creativity is welcome, but the card must maintain a polished and professional appearance.

Details to Include:

Name: Gavin Trelowe
Title: VP Sales / Operations
Company: Valtrim Systems
Phone: 483.216.7705
Email: gavin@valtrimsystems-example.com
Website: www.valtrimsystems-example.com

```html
<!DOCTYPE html>
<html lang="en">
<head>
<meta charset="utf-8">
<title>Valtrim Systems – Business Card</title>
<link href="https://fonts.googleapis.com/css2?family=Poppins:wght@300;400;600;700&display=swap" rel="stylesheet">
<style>
  :root {
    --stage: #222222;
    --card: #ffffff;
    --brand-blue: #1474c4;
    --ink: #111111;
  }
  * { margin: 0; padding: 0; box-sizing: border-box; }
  html, body { width: 1200px; height: 711px; overflow: hidden; }
  body {
    background: var(--stage);
    font-family: 'Poppins', sans-serif;
    color: var(--ink);
    position: relative;
  }
  .card {
    position: absolute;
    top: 200px;
    width: 540px;
    height: 309px;
    background: var(--card);
    overflow: hidden;
  }
  .card--front { left: 40px; }
  .card--back { left: 620px; }

  .edge-band {
    position: absolute;
    width: 10px;
    background: var(--brand-blue);
  }
  .edge-band--right { right: 0; top: 28px; height: 130px; }
  .edge-band--left { left: 0; top: 150px; height: 130px; }

  .wordmark {
    position: absolute;
    font-weight: 700;
    color: var(--ink);
    letter-spacing: 1px;
    white-space: nowrap;
  }
  .card--front .wordmark {
    left: 0; right: 0; top: 126px;
    text-align: center;
    font-size: 42px;
  }
  .card--back .wordmark {
    left: 34px; top: 138px;
    font-size: 21px;
    letter-spacing: 0.5px;
  }

  .divider {
    position: absolute;
    left: 250px;
    top: 60px;
    width: 1px;
    height: 150px;
    background: var(--brand-blue);
  }

  .contact-block {
    position: absolute;
    left: 266px;
    top: 62px;
  }
  .person-name {
    font-size: 24px;
    line-height: 1.1;
    white-space: nowrap;
  }
  .person-name .first { font-weight: 700; color: var(--brand-blue); }
  .person-name .last { font-weight: 300; color: var(--ink); }
  .person-title {
    font-size: 11px;
    font-weight: 600;
    margin: 2px 0 0 12px;
  }
  .contact-list {
    list-style: none;
    margin: 24px 0 0 14px;
    font-size: 11px;
    font-weight: 400;
    line-height: 20px;
  }
  .contact-list li { display: flex; align-items: center; gap: 7px; white-space: nowrap; }
  .contact-list svg { width: 11px; height: 11px; fill: var(--brand-blue); flex: none; }

  .address {
    position: absolute;
    left: 150px;
    bottom: 34px;
    font-size: 12px;
    font-weight: 400;
    color: var(--brand-blue);
    white-space: nowrap;
  }
</style>
</head>
<body>
  <section class="card card--front" aria-label="Card front">
    <span class="edge-band edge-band--right"></span>
    <span class="edge-band edge-band--left"></span>
    <h1 class="wordmark">Valtrim Systems</h1>
  </section>

  <section class="card card--back" aria-label="Card back">
    <span class="edge-band edge-band--right"></span>
    <span class="edge-band edge-band--left"></span>
    <div class="wordmark">Valtrim Systems</div>
    <span class="divider"></span>

    <div class="contact-block">
      <p class="person-name"><span class="first">Gavin</span> <span class="last">Trelowe</span></p>
      <p class="person-title">VP Sales / Operations</p>
      <ul class="contact-list">
        <li>
          <svg viewBox="0 0 24 24" aria-hidden="true"><path d="M6.6 10.8a15 15 0 0 0 6.6 6.6l2.2-2.2a1 1 0 0 1 1-.25 11.4 11.4 0 0 0 3.6.57 1 1 0 0 1 1 1V20a1 1 0 0 1-1 1A17 17 0 0 1 3 4a1 1 0 0 1 1-1h3.5a1 1 0 0 1 1 1c0 1.25.2 2.45.57 3.570a1 1 0 0 1-.25 1z"/></svg>
          483.216.7705
        </li>
        <li>
          <svg viewBox="0 0 24 24" aria-hidden="true"><path d="M12 2a10 10 0 1 0 0 20 10 10 0 0 0 0-20zm-1 17.9A8 8 0 0 1 4.1 10.9L9 15.8v1a2 2 0 0 0 2 2zm6.9-2.5A2 2 0 0 0 16 16h-1v-3a1 1 0 0 0-1-1H8v-2h2a1 1 0 0 0 1-1V7h2a2 2 0 0 0 2-2v-.4a8 8 0 0 1 2.9 12.8z"/></svg>
          www.valtrimsystems-example.com
        </li>
        <li>
          <svg viewBox="0 0 24 24" aria-hidden="true"><path d="M2 6a2 2 0 0 1 2-2h16a2 2 0 0 1 2 2v12a2 2 0 0 1-2 2H4a2 2 0 0 1-2-2zm2 .5V7l8 5 8-5v-.5z"/></svg>
          gavin@valtrimsystems-example.com
        </li>
      </ul>
    </div>

    <p class="address">48 Harrow Lane, Brenton, VA 20199 United States</p>
  </section>
</body>
</html>
```